iOS App Design Project for Pebble Tasks

We are looking for a redesign of the UI for our app, Pebble Tasks. The app is a to-do list type app with 4 screens, and we already have a UI for it but we would like a nicer looking one that has a better colour scheme and is more intuitive.

We would like something that is a real treat to look at, and that users really want to use. Essentially what we want is the nicest and most simple design possible, as the current UI we have is not very user friendly.

The app is already on the market and is free so if you have an iOS device you can download it and take a look at it, and we have also included screenshots of the app.
Updates

Project Deadline Extended
Reason: I am updating the design brief and will also guarantee the payment.

Target Market(s)

Mobile users looking for simplicity

Requirements
Must have
• - Very visually pleasing
- Simple layout with minimal clutter
- Icons and buttons that explain what they do
Should not have
• Any features that detract from the simplicity of the app are not wanted.

```html
<!DOCTYPE html>
<html lang="en">
<head>
<meta charset="utf-8">
<title>Tidy Tasks – Task</title>
<link rel="stylesheet" href="https://fonts.googleapis.com/css2?family=Exo+2:wght@400;500;600&family=Roboto+Condensed:wght@700&display=swap">
<style>
  :root {
    --bar-top: #2a2a2a;
    --bar-bottom: #050505;
    --glow: #2fb6d6;
    --canvas: #f2f2f2;
    --pill-top: #3a3a3a;
    --pill-bottom: #1e1e1e;
    --pill-edge: #585858;
    --text-light: #ffffff;
    --text-muted: #8a8a8a;
    --panel: #2b2b2b;
    --panel-edge: #6a6a6a;
    --tab-bg: #141414;
    --tab-active: #f4f4f4;
    --tab-label: #d8d8d8;
    --tab-label-active: #2a2a2a;
  }
  * { box-sizing: border-box; margin: 0; padding: 0; }
  html, body { width: 800px; height: 1200px; overflow: hidden; }
  body {
    position: relative;
    background: var(--canvas);
    font-family: "Exo 2", "Trebuchet MS", sans-serif;
    color: var(--text-light);
  }
  .nav-bar {
    position: absolute; left: 0; top: 0; width: 800px; height: 106px;
    background:
      radial-gradient(ellipse 260px 18px at 50% 0, rgba(47,182,214,.55), transparent 100%),
      linear-gradient(var(--bar-top), var(--bar-bottom));
    box-shadow: 0 4px 8px rgba(0,0,0,.35);
  }
  .nav-title {
    position: absolute; left: 0; right: 0; top: 32px;
    text-align: center; font-size: 38px; font-weight: 500; letter-spacing: 1px;
  }
  .nav-button {
    position: absolute; top: 17px; height: 71px;
    display: flex; align-items: center; justify-content: center;
    font-size: 32px; font-weight: 500;
    background: linear-gradient(#4a4a4a, #262626);
  }
  .nav-button.back { left: 15px; width: 120px; padding-left: 10px;
    clip-path: polygon(18px 0, 100% 0, 100% 100%, 18px 100%, 0 50%); border-radius: 6px; }
  .nav-button.next { left: 652px; width: 123px; padding-right: 10px;
    clip-path: polygon(0 0, calc(100% - 18px) 0, 100% 50%, calc(100% - 18px) 100%, 0 100%); border-radius: 6px; }

  .add-button {
    position: absolute; left: 681px; top: 129px; width: 94px; height: 77px;
    border-radius: 10px; background: linear-gradient(#454545, #1d1d1d);
    border: 2px solid #cfcfcf; box-shadow: 0 3px 6px rgba(0,0,0,.35);
    display: flex; align-items: center; justify-content: center;
  }

  .task-pill {
    position: absolute; height: 99px; border-radius: 50px;
    background: linear-gradient(var(--pill-top) 0%, #2c2c2c 50%, var(--pill-bottom) 51%, #262626 100%);
    border: 3px solid var(--pill-edge);
    box-shadow: 0 2px 4px rgba(0,0,0,.3);
    display: flex; align-items: center; justify-content: center;
    font-size: 38px; font-weight: 500; letter-spacing: .5px;
  }
  .task-pill.selected {
    left: 25px; top: 304px; width: 600px;
    box-shadow: 0 -6px 14px rgba(47,182,214,.45), 0 6px 14px rgba(47,182,214,.45);
    border-color: #4a4a4a;
  }
  .task-pill.regular { left: 56px; width: 602px; }

  .pointer { position: absolute; left: 640px; top: 336px; }

  .action-panel {
    position: absolute; left: 671px; top: 237px; width: 113px; height: 788px;
    background: var(--panel); border: 2px solid var(--panel-edge); border-radius: 8px;
  }
  .action {
    position: absolute; left: 9px; width: 95px; height: 94px;
    border-radius: 8px; background: linear-gradient(#474747, #2a2a2a);
    border: 1px solid #555;
    display: flex; align-items: center; justify-content: center;
    font-size: 28px; color: var(--text-light);
  }
  .action.active { border: 2px solid var(--glow); color: #7fd8ee;
    background: linear-gradient(#3a3a3a, #1a1a1a); }
  .action.disabled { color: var(--text-muted); background: linear-gradient(#3a3a3a, #2e2e2e); }
  .divider { position: absolute; left: 14px; width: 85px; height: 2px; background: #5c5c5c; }

  .tab-bar {
    position: absolute; left: 0; top: 1078px; width: 800px; height: 122px;
    background: linear-gradient(#2a2a2a, var(--tab-bg));
  }
  .tab {
    position: absolute; top: 0; height: 122px; width: 200px;
    display: flex; flex-direction: column; align-items: center; justify-content: flex-end;
    padding-bottom: 6px;
    font-family: "Roboto Condensed", "Arial Narrow", sans-serif; font-weight: 700;
    font-size: 25px; color: var(--tab-label);
  }
  .tab svg { margin-bottom: 4px; }
  .tab.active { background: var(--tab-active); color: var(--tab-label-active);
    border-bottom: 4px solid var(--glow); border-radius: 4px 4px 0 0; }
</style>
</head>
<body>
  <header class="nav-bar">
    <div class="nav-button back">Back</div>
    <div class="nav-title">TASK</div>
    <div class="nav-button next">Next</div>
  </header>

  <div class="add-button" aria-label="Add task">
    <svg width="40" height="40" viewBox="0 0 40 40"><path d="M20 4v32M4 20h32" stroke="#fff" stroke-width="6" stroke-linecap="round"/></svg>
  </div>

  <div class="task-pill selected">Shopping</div>
  <div class="task-pill regular" style="top:441px">Homework</div>
  <div class="task-pill regular" style="top:579px">Task</div>
  <div class="task-pill regular" style="top:716px">Task</div>
  <div class="task-pill regular" style="top:854px">Task</div>

  <svg class="pointer" width="33" height="42" viewBox="0 0 33 42">
    <path d="M33 0 L0 21 L33 42 Z" fill="var(--panel)" stroke="var(--panel-edge)" stroke-width="2"/>
  </svg>

  <nav class="action-panel">
    <div class="action active" style="top:8px">Edit</div>
    <div class="divider" style="top:117px"></div>
    <div class="action" style="top:132px">OFF</div>
    <div class="action disabled" style="top:238px">ON</div>
    <div class="action" style="top:343px">Time</div>
    <div class="action" style="top:450px">Add</div>
    <div class="divider" style="top:557px"></div>
    <div class="action" style="top:572px">Delete</div>
    <div class="action" style="top:677px">Save</div>
  </nav>

  <footer class="tab-bar">
    <div class="tab" style="left:0">
      <svg width="56" height="70" viewBox="0 0 56 70"><path d="M8 6h40l-4 58H4z" fill="#9a9a9a" stroke="#555" stroke-width="2"/><path d="M14 20h28M13 30h28M12 40h28M11 50h28" stroke="#333" stroke-width="4"/></svg>
      LIST
    </div>
    <div class="tab active" style="left:202px;width:191px">
      <svg width="70" height="70" viewBox="0 0 70 70"><ellipse cx="46" cy="58" rx="20" ry="6" fill="#c9c9c9"/><path d="M18 6h32l-6 56H12z" fill="#fff" stroke="#333" stroke-width="3"/><path d="M22 34l7 9 14-22" fill="none" stroke="#333" stroke-width="3.5"/></svg>
      TASK
    </div>
    <div class="tab" style="left:400px">
      <svg width="56" height="70" viewBox="0 0 56 70"><path d="M8 6h36l4 58H12z" fill="#9a9a9a" stroke="#555" stroke-width="2"/><path d="M16 20h24M17 30h24M18 40h24M19 50h24" stroke="#333" stroke-width="3"/></svg>
      NOTE
    </div>
    <div class="tab" style="left:600px">
      <svg width="62" height="62" viewBox="0 0 62 62"><circle cx="31" cy="31" r="26" fill="#9a9a9a" stroke="#555" stroke-width="3"/><path d="M31 16v30M16 31h30" stroke="#2a2a2a" stroke-width="5"/></svg>
      MORE
    </div>
  </footer>
</body>
</html>
```